A label for a massage gel with bee venom for chronic pain

The product is a massage gel with natural ingredients that contain beehive products (propolis, bee venom, bee wax) and has an effect similar to Kivo Mast.

The product is packed in a 250 ml plastic jar, and we need a proper label.

```html
<!DOCTYPE html>
<html lang="en">
<head>
<meta charset="utf-8">
<title>Massage Gel – Jar Label</title>
<link rel="stylesheet" href="https://fonts.googleapis.com/css2?family=Bebas+Neue&family=Oswald:wght@400;500&family=Roboto:ital,wght@0,400;0,500;1,700;1,900&display=swap">
<style>
  :root {
    --page: #ffffff;
    --red-light: #e8394c;
    --red: #d81d2c;
    --red-deep: #c50f1c;
    --green-dark: #116b45;
    --green: #10894c;
    --green-light: #129450;
    --white: #ffffff;
    --rule: rgba(255,255,255,0.75);
    --figure-hot: #e41b1b;
    --figure-warm: #f49a1c;
    --figure-sun: #f7dc2a;
  }
  * { box-sizing: border-box; margin: 0; padding: 0; }
  html, body { width: 1200px; height: 770px; overflow: hidden; background: var(--page); }
  .canvas { position: relative; width: 1200px; height: 770px; }

  .label {
    position: absolute; left: 20px; top: 141px;
    width: 950px; height: 400px;
    transform: scale(1.2211); transform-origin: 0 0;
    overflow: hidden;
    background: linear-gradient(90deg, var(--red-light) 0%, var(--red) 55%, var(--red-deep) 100%);
    box-shadow: 0 1px 3px rgba(0,0,0,0.25);
    color: var(--white);
  }

  .band-title {
    position: absolute; left: 0; top: 92px; width: 100%; height: 84px;
    background: linear-gradient(90deg, var(--green-dark) 0%, var(--green) 50%, var(--green-light) 100%);
    border-top: 2px solid var(--rule); border-bottom: 2px solid var(--rule);
  }
  .band-footer {
    position: absolute; left: 0; top: 345px; width: 100%; height: 55px;
    background: linear-gradient(90deg, var(--green-dark) 0%, var(--green) 50%, var(--green-light) 100%);
  }

  .figure-art { position: absolute; left: 598px; top: 10px; width: 186px; height: 390px; z-index: 1; }

  .text-layer { position: absolute; inset: 0; z-index: 2; }

  .brand {
    position: absolute; left: 352px; top: 18px; width: 200px;
    text-align: center; font-family: "Roboto", sans-serif; font-weight: 400;
    font-size: 17px; line-height: 18px; letter-spacing: 2px;
  }
  .brand .brand-main { font-family: "Oswald", sans-serif; font-weight: 500; font-size: 22px; line-height: 22px; letter-spacing: 1px; }

  .product-name {
    position: absolute; left: 222px; top: 96px; width: 366px;
    text-align: center; font-family: "Bebas Neue", sans-serif; font-weight: 400;
    font-size: 70px; line-height: 72px; letter-spacing: 0.5px;
  }
  .product-sub {
    position: absolute; left: 222px; top: 157px; width: 366px;
    text-align: center; font-family: "Roboto", sans-serif; font-weight: 500;
    font-size: 14px; letter-spacing: 3px;
  }

  .uses {
    position: absolute; left: 345px; top: 194px; list-style: none;
    font-family: "Roboto", sans-serif; font-style: italic; font-weight: 700;
    font-size: 23px; line-height: 26.5px;
  }
  .uses::before {
    content: ""; position: absolute; left: 5px; top: 12px; width: 2px; height: 80px; background: var(--white);
  }
  .uses li { position: relative; padding-left: 22px; }
  .uses li::before {
    content: ""; position: absolute; left: 1px; top: 9px; width: 10px; height: 10px; border-radius: 50%; background: var(--white);
  }

  .net-weight {
    position: absolute; left: 267px; top: 318px;
    font-family: "Oswald", sans-serif; font-weight: 400; font-size: 17px; letter-spacing: -0.3px;
  }

  .ingredients {
    position: absolute; left: 270px; top: 358px; display: flex; align-items: center; gap: 7px;
    font-family: "Oswald", sans-serif; font-weight: 500; font-size: 18px; letter-spacing: -0.3px;
  }
  .ingredients .leaf { width: 22px; height: 22px; }
  .ingredients .with-tag {
    background: var(--white); color: var(--green);
    font-family: "Roboto", sans-serif; font-style: italic; font-weight: 900; font-size: 13px;
    padding: 1px 5px; line-height: 15px;
  }
</style>
</head>
<body>
<div class="canvas">
  <div class="label">
    <div class="band-title"></div>
    <div class="band-footer"></div>

    <svg class="figure-art" viewBox="0 0 186 390" role="img" aria-label="Illustration of a standing human figure in red-to-yellow faceted heat tones with glowing pain points at neck, back, elbow and knee">
      <defs>
        <linearGradient id="heat" x1="0" y1="0" x2="0.4" y2="1">
          <stop offset="0" stop-color="#e41b1b"/>
          <stop offset="0.45" stop-color="#f49a1c"/>
          <stop offset="1" stop-color="#f7dc2a"/>
        </linearGradient>
      </defs>
      <rect x="0" y="0" width="186" height="390" rx="20" fill="url(#heat)"/>
    </svg>

    <div class="text-layer">
      <div class="brand">YOUR<br><span class="brand-main">-LOGO-</span><br>HERE</div>

      <h1 class="product-name">MASSAGE GEL</h1>
      <p class="product-sub">PAIN RELIEVING CREAM</p>

      <ul class="uses">
        <li>Backache</li>
        <li>Stiff Neck</li>
        <li>Joint Pain</li>
        <li>Sore Muscle</li>
      </ul>

      <p class="net-weight">NET WT 3 OZ (85 g)</p>

      <div class="ingredients">
        <svg class="leaf" viewBox="0 0 22 22" aria-hidden="true">
          <path d="M3 19 C3 8 10 2 20 2 C20 12 14 19 3 19 Z" fill="#ffffff"/>
          <path d="M4 18 C8 12 12 8 17 5" stroke="#10894c" stroke-width="1.6" fill="none"/>
        </svg>
        <span class="with-tag">WITH:</span>
        <span class="ingredient-list">PROPOLIS, BEE VENOM &amp; BEE WAX.</span>
      </div>
    </div>
  </div>
</div>
</body>
</html>
```